Business card design for Luxury Real Estate

Using the corporate logo you have designed, please design a business card for a luxury real estate company in Thailand.

The brand is about elegance, calm, sophistication and luxury. The card should look clean, modern and be standard business card size. The background should be white to enable future scanning of the card (funky backgrounds result in poor card scanning results).

Text on Business Card (Front side) shall include the following:
- Corporate Logo
- Include the following business services underneath " Sales. Rentals. Investments. Financing."
- Name: Marisa Tovel
- Title: CEO, Founder
- mobile phone: +65 83920516 (Singapore), +66 6000 48270 (Thailand)
- email: marisa@brightharborestates.example
- skype: brightharborestates
- url: www.brightharborestates.example

Backside
- include same info but shall have Chinese name and title.
Updates

please use the attached additional language in mandarin for "sales. rentals. investments. financing."

Target Market(s)

high net worth individuals, business men/ women, finance managers.

Industry/Entity Type

Real Estate

Requirements
Must have
• elegant, sophisticated, clean, modern look. appealing but comforting to the eye. should not be crowded and overcomplicated.

```html
<!DOCTYPE html>
<html lang="en">
<head>
<meta charset="utf-8">
<title>Bright Harbor Estates – Business Card</title>
<link rel="stylesheet" href="https://fonts.googleapis.com/css2?family=Lato:wght@400;700&family=Noto+Sans+SC:wght@400;700&display=swap">
<style>
  :root {
    --backdrop: #a7a8aa;
    --card: #ffffff;
    --ink: #1a1a1a;
    --gold: #d9a24e;
    --shadow: rgba(40, 40, 40, 0.75);
  }
  * { margin: 0; padding: 0; box-sizing: border-box; }
  html, body {
    width: 922px;
    height: 1200px;
    overflow: hidden;
    background: var(--backdrop);
  }
  .sheet {
    position: relative;
    width: 922px;
    height: 1200px;
  }
  .card {
    position: absolute;
    left: 123px;
    width: 650px;
    height: 420px;
    background: var(--card);
    box-shadow: 16px 12px 10px var(--shadow);
    font-family: "Lato", "Noto Sans SC", sans-serif;
    color: var(--ink);
  }
  .card--front { top: 116px; }
  .card--back { top: 607px; }

  .identity {
    position: absolute;
    left: 358px;
    top: 32px;
  }
  .identity__name {
    font-size: 24px;
    font-weight: 700;
    letter-spacing: 0.1px;
    line-height: 30px;
  }
  .identity__title {
    font-size: 17px;
    font-weight: 400;
    line-height: 24px;
  }
  .card--back .identity__name,
  .card--back .identity__title {
    font-family: "Noto Sans SC", sans-serif;
  }
  .card--back .identity__name { font-size: 22px; }
  .card--back .identity__title { font-size: 16px; }

  .contacts {
    position: absolute;
    left: 358px;
    top: 118px;
    list-style: none;
  }
  .contacts__row {
    position: relative;
    height: 25px;
    padding-left: 27px;
    font-size: 15px;
    line-height: 22px;
  }
  .contacts__row--tight { height: 22px; }
  .contacts__label {
    position: absolute;
    left: 0;
    top: 1px;
    font-size: 10px;
    letter-spacing: 0.5px;
  }
  .contacts__row::before {
    content: "";
    position: absolute;
    left: 16px;
    top: 10px;
    width: 4px;
    height: 4px;
    border-radius: 50%;
    background: var(--gold);
  }

  .brand {
    position: absolute;
    left: 28px;
    top: 292px;
    display: flex;
    align-items: center;
    gap: 10px;
  }
  .brand__dot {
    width: 12px;
    height: 12px;
    border-radius: 50%;
    background: var(--gold);
  }
  .brand__name {
    font-size: 30px;
    font-weight: 400;
    color: var(--ink);
    letter-spacing: 0.2px;
  }
  .brand__rule {
    position: absolute;
    left: 28px;
    top: 345px;
    width: 248px;
    height: 1px;
    background: var(--ink);
  }

  .services {
    position: absolute;
    left: 28px;
    top: 376px;
    font-size: 13px;
    letter-spacing: 2.6px;
    display: flex;
    align-items: center;
    gap: 7px;
    white-space: nowrap;
  }
  .services__sep {
    width: 5px;
    height: 5px;
    border-radius: 50%;
    background: var(--gold);
  }
</style>
</head>
<body>
<main class="sheet">

  <section class="card card--front" aria-label="Business card, English side">
    <div class="identity">
      <p class="identity__name">Marisa Tovel</p>
      <p class="identity__title">CEO, Founder</p>
    </div>
    <ul class="contacts">
      <li class="contacts__row contacts__row--tight"><span class="contacts__label">T</span>+65 83920516 (Singapore)</li>
      <li class="contacts__row">+66 6000 48270 (Thailand)</li>
      <li class="contacts__row"><span class="contacts__label">E</span>marisa@brightharborestates.example</li>
      <li class="contacts__row"><span class="contacts__label">S</span>brightharborestates</li>
      <li class="contacts__row"><span class="contacts__label">W</span>www.brightharborestates.example</li>
    </ul>
    <div class="brand">
      <span class="brand__dot"></span>
      <span class="brand__name">Bright Harbor Estates</span>
    </div>
    <div class="brand__rule"></div>
    <p class="services">
      <span>SALES</span><span class="services__sep"></span>
      <span>RENTALS</span><span class="services__sep"></span>
      <span>INVESTMENTS</span><span class="services__sep"></span>
      <span>FINANCING</span>
    </p>
  </section>

  <section class="card card--back" aria-label="Business card, Chinese side">
    <div class="identity">
      <p class="identity__name" lang="zh">陶玛丽</p>
      <p class="identity__title" lang="zh">总裁</p>
    </div>
    <ul class="contacts">
      <li class="contacts__row contacts__row--tight"><span class="contacts__label">T</span>+65 83920516 (Singapore)</li>
      <li class="contacts__row">+66 6000 48270 (Thailand)</li>
      <li class="contacts__row"><span class="contacts__label">E</span>marisa@brightharborestates.example</li>
      <li class="contacts__row"><span class="contacts__label">S</span>brightharborestates</li>
      <li class="contacts__row"><span class="contacts__label">W</span>www.brightharborestates.example</li>
    </ul>
    <div class="brand">
      <span class="brand__dot"></span>
      <span class="brand__name">Bright Harbor Estates</span>
    </div>
    <div class="brand__rule"></div>
    <p class="services">
      <span>SALES</span><span class="services__sep"></span>
      <span>RENTALS</span><span class="services__sep"></span>
      <span>INVESTMENTS</span><span class="services__sep"></span>
      <span>FINANCING</span>
    </p>
  </section>

</main>
</body>
</html>
```